We need a home page that represents us as the best Veterinary Hospital in the State

We need webdesign for a Vet Hospital in Rio de Janeiro, Brazil.
We think the current design is very childish. We want something that looks more like a hospital and not a clinic.
We put a map to guide the content of the sections and also an example of a layout that we don't like but that may serve as a reference as a wireframe.

Target Market(s)

pet owners

Industry/Entity Type

Pet Care

Number of Pages Required

1 page

Requirements
Must have
• Here is a map of the sections and texts we think for home: https://qx.vz/5719382046?t=PlorvKanbe
Nice to have
• some sites we like:
https://www.valtorim.br/Pages/Home.aspx
https://www.pelmarvito.com/
Should not have
• This is a design that we started working on and the content is correct. But the layout is poor in detail, bad colors, CTA's without prominence.

https://ronalbekwistudio.plotvarex.com/console/share/KT7N9H2WRM/918273645

```html
<!DOCTYPE html>
<html lang="en">
<head>
<meta charset="utf-8">
<title>Vela Pet 24h</title>
<link href="https://fonts.googleapis.com/css2?family=Montserrat:wght@500;600;700&family=Open+Sans:ital,wght@0,400;0,600;1,400&display=swap" rel="stylesheet">
<style>
:root{
  --blue:#0b7cc6;
  --blue-dark:#1767a8;
  --red:#e41d3d;
  --ink:#2b2b2b;
  --text:#444;
  --muted:#666;
  --footer:#0e0e0f;
  --white:#fff;
}
*{margin:0;padding:0;box-sizing:border-box}
html,body{width:1200px;height:3640px;overflow:hidden}
body{position:relative;background:var(--white);font-family:"Open Sans",sans-serif;color:var(--text)}
.abs{position:absolute}
h1,h2,h3,h4,.btn,.brand{font-family:"Montserrat",sans-serif}
.brand{font-weight:700;color:var(--blue);display:flex;align-items:center;gap:10px}
.brand i{display:block;background:var(--red)}
.btn{position:absolute;display:flex;align-items:center;justify-content:center;border-radius:32px;font-weight:600;font-size:17px;color:var(--white);text-transform:uppercase;letter-spacing:-.2px}
.btn-red{background:var(--red)}
.btn-ghost{border:2px solid var(--white)}

/* header */
.site-header{top:0;left:0;width:1200px;height:99px;background:var(--white)}
.site-header .brand{left:110px;top:30px;font-size:34px}
.site-header .brand i{width:22px;height:22px}
.main-nav{right:40px;top:38px;display:flex;gap:18px;font-size:14.5px;color:#333}

/* hero */
.hero{top:99px;left:0;width:1200px;height:610px;overflow:hidden}
.hero-bg{position:absolute;inset:0;background:linear-gradient(100deg,#2f7cc0 0%,#4a86c4 45%,#7f7fb6 75%,#b67b9e 100%)}
.hero h1{left:109px;top:90px;font-size:34px;line-height:46px;font-weight:600;letter-spacing:-.6px;color:var(--white);white-space:nowrap;z-index:2}
.hero p{left:110px;top:246px;font-size:20px;line-height:32px;color:var(--white);width:500px}
.hero .pet{border-radius:14px}
.wave{position:absolute;left:0}

/* units */
.units-title{top:732px;width:1200px;text-align:center;font-size:33px;font-weight:600;color:var(--ink)}
.unit{top:813px;width:309px}
.unit .photo{height:278px;border-radius:12px 12px 0 0}
.unit .tag{position:absolute;top:250px;left:42px;width:226px;height:54px;border-radius:14px;display:flex;align-items:center;justify-content:center;color:var(--white);font-size:23px;font-family:"Open Sans",sans-serif;font-weight:600}
.unit .desc{margin-top:54px;font-size:16px;line-height:23px;color:#333;font-weight:600}
.unit .addr{margin-top:25px;font-size:15px;line-height:23px;color:#555;display:flex;gap:10px}
.unit .addr svg{flex:none;margin-top:3px}

/* infrastructure */
.infra-bg{top:1329px;left:0;width:1200px;height:486px;background:linear-gradient(90deg,#e6edf3,#eef2f6 40%,#dfe8ef)}
.infra h2{top:1468px;width:1200px;text-align:center;font-size:35px;line-height:46px;font-weight:600;color:var(--ink)}
.infra p{top:1580px;width:1200px;text-align:center;font-size:16px;color:#555}
.video{left:290px;top:1744px;width:619px;height:372px;background:linear-gradient(110deg,#c9d3dd,#e6e9ee 45%,#9bb0c2);box-shadow:0 6px 18px rgba(0,0,0,.15)}

/* testimonial */
.testi-photo{top:2188px;left:0;width:478px;height:449px;background:linear-gradient(135deg,#5f7f95,#a8825e 55%,#d7d2cb)}
.testi{top:2188px;left:478px;width:722px;height:449px;background:var(--blue)}
.testi h2{position:absolute;left:63px;top:52px;font-size:35px;font-weight:600;color:var(--white)}
.testi blockquote{position:absolute;left:63px;top:112px;width:560px;font-style:italic;font-size:20.5px;line-height:34.5px;color:var(--white)}
.testi .author{position:absolute;left:63px;top:305px;display:flex;align-items:center;gap:20px;color:var(--white);font-size:19px;font-weight:600}
.testi .avatar{width:88px;height:88px;border-radius:50%;background:linear-gradient(135deg,#7b4a33,#c58a63)}
.testi .arrows{position:absolute;left:563px;top:340px;display:flex;gap:8px}

/* blog */
.blog-intro{left:109px;top:2705px}
.blog-intro .kicker{font-size:27px;color:#333;font-family:"Montserrat",sans-serif;font-weight:500}
.blog-intro h2{font-size:34px;line-height:46px;font-weight:600;color:var(--ink);margin-top:4px}
.post{top:2700px;width:278px}
.post .thumb{height:200px;border-radius:12px}
.post h3{margin-top:20px;font-size:18px;line-height:25px;font-weight:500;color:#333}
.post .date{margin-top:14px;font-size:16px;color:#777;display:flex;align-items:center;gap:8px}

/* footer */
.footer-bg{top:3030px;left:0;width:1200px;height:610px}
.footer-brand{left:113px;top:3215px;font-size:46px}
.footer-brand i{width:30px;height:30px}
.footer-about{left:113px;top:3316px;width:320px;font-size:16px;line-height:27.5px;color:#eee}
.footer-about .line{display:flex;align-items:center;gap:8px}
.fcol{top:3213px}
.fcol h4{font-size:19px;font-weight:600;color:var(--white);margin-bottom:8px}
.fcol li{list-style:none;font-size:16px;line-height:27.6px;color:#e5e5e5}
.footer-rule{left:113px;top:3550px;width:975px;height:1px;background:#333}
.copyright{left:113px;top:3575px;font-size:16px;color:#eee}
.follow{left:742px;top:3569px;display:flex;align-items:center;gap:0}
.follow span{font-family:"Montserrat",sans-serif;font-weight:600;font-size:19px;color:var(--white);margin-right:20px}
.follow i{display:block;width:46px;height:46px;border:2px solid var(--white);border-radius:50%;margin-right:8px}
</style>
</head>
<body>

<header class="site-header abs">
  <div class="brand abs">Vela Pet <i></i></div>
  <nav class="main-nav abs">
    <span>Units</span><span>Schedules</span><span>Specialties</span><span>Blog</span><span>Vaccines</span><span>Work with us</span><span>A Vela Pet</span><span>Tutor Area</span><span>Team</span>
  </nav>
</header>

<section class="hero abs">
  <div class="hero-bg"></div>
  <div class="pet abs" role="img" aria-label="Photo of a grey and white cat" style="left:608px;top:141px;width:209px;height:202px;background:linear-gradient(135deg,#7a8597,#b4bccb)"></div>
  <div class="pet abs" role="img" aria-label="Photo of a golden retriever resting its head" style="left:837px;top:188px;width:275px;height:264px;background:linear-gradient(135deg,#c68a5b,#8e5535)"></div>
  <h1 class="abs">Dedication 24 hours a day<br>7 days a week to take care<br>of those you love!</h1>
  <p class="abs">Excellent doctors and complete infrastructure at a price that fits in your pocket.</p>
  <div class="btn btn-red" style="left:112px;top:346px;width:202px;height:64px">Emergency Room</div>
  <div class="btn btn-ghost" style="left:326px;top:346px;width:159px;height:64px">Queries</div>
  <svg class="wave" style="top:480px" width="1200" height="130" viewBox="0 0 1200 130">
    <path d="M0 8 C120 70 260 120 430 114 C600 108 690 10 860 20 C1000 28 1100 80 1200 122 L1200 130 L0 130 Z" fill="#fff"/>
  </svg>
</section>

<h2 class="units-title abs">Vela Pet Units</h2>

<article class="unit abs" style="left:112px">
  <div class="photo" role="img" aria-label="Hospital building facade with H sign" style="background:linear-gradient(160deg,#3b7fd0,#cfd9e6 70%)"></div>
  <div class="tag" style="background:var(--blue)">Taquara - RJ</div>
  <p class="desc">Emergency Room, Clinical Care and Specialties</p>
  <div class="addr"><svg width="11" height="15" viewBox="0 0 11 15"><path d="M5.5 0A5.5 5.5 0 0 0 0 5.5C0 9.5 5.5 15 5.5 15S11 9.5 11 5.5A5.5 5.5 0 0 0 5.5 0Zm0 7.6a2.1 2.1 0 1 1 0-4.2 2.1 2.1 0 0 1 0 4.2Z" fill="#e41d3d"/></svg><span>Rua Almirante Sereno, 58 -<br>Copacabana, Rio<br>de Janeiro - RJ, 22040-110</span></div>
</article>
<article class="unit abs" style="left:445px">
  <div class="photo" role="img" aria-label="Clinic entrance with glass doors" style="background:linear-gradient(160deg,#e3e3e0,#a9a69d)"></div>
  <div class="tag" style="background:var(--red)">Flamengo - RJ</div>
  <p class="desc">Emergency Room, Clinical Care and Specialties</p>
  <div class="addr"><svg width="11" height="15" viewBox="0 0 11 15"><path d="M5.5 0A5.5 5.5 0 0 0 0 5.5C0 9.5 5.5 15 5.5 15S11 9.5 11 5.5A5.5 5.5 0 0 0 5.5 0Zm0 7.6a2.1 2.1 0 1 1 0-4.2 2.1 2.1 0 0 1 0 4.2Z" fill="#e41d3d"/></svg><span>Rua Almirante Sereno, 58 -<br>Copacabana, Rio<br>de Janeiro - RJ, 22040-110</span></div>
</article>
<article class="unit abs" style="left:779px">
  <div class="photo" role="img" aria-label="Red brick emergency entrance" style="background:linear-gradient(170deg,#2a8a78,#9c4a38 35%,#b9a58a 80%,#e6e6e6)"></div>
  <div class="tag" style="background:var(--blue)">Copacabana - RJ</div>
  <p class="desc">Emergency Room, Clinical Care and Specialties</p>
  <div class="addr"><svg width="11" height="15" viewBox="0 0 11 15"><path d="M5.5 0A5.5 5.5 0 0 0 0 5.5C0 9.5 5.5 15 5.5 15S11 9.5 11 5.5A5.5 5.5 0 0 0 5.5 0Zm0 7.6a2.1 2.1 0 1 1 0-4.2 2.1 2.1 0 0 1 0 4.2Z" fill="#e41d3d"/></svg><span>Rua Almirante Sereno, 58 -<br>Copacabana, Rio<br>de Janeiro - RJ, 22040-110</span></div>
</article>

<section class="infra">
  <div class="infra-bg abs" role="img" aria-label="Faded photo of a veterinary hospital interior with staff"></div>
  <svg class="wave" style="top:1320px" width="1200" height="110" viewBox="0 0 1200 110">
    <path d="M0 0 L1200 0 L1200 20 C1080 70 960 80 820 62 C660 40 560 20 400 30 C240 40 120 80 0 110 Z" fill="#fff"/>
  </svg>
  <h2 class="abs">Complete Infrastructure And Medical Staff<br>Available 24 Hours Every Day</h2>
  <p class="abs">Emergency room, detention center, imaging exams. surgery.</p>
  <div class="btn btn-red" style="left:499px;top:1640px;width:201px;height:62px">See the video</div>
  <div class="video abs" role="img" aria-label="Video still of two veterinarians in white coats and masks"></div>
  <svg class="abs" style="left:569px;top:1897px" width="64" height="64" viewBox="0 0 64 64"><circle cx="32" cy="32" r="32" fill="#111"/><path d="M25 19 L46 32 L25 45 Z" fill="#fff"/></svg>
</section>

<div class="testi-photo abs" role="img" aria-label="Veterinarian petting a husky dog"></div>
<section class="testi abs">
  <h2>What Some Tutors Say</h2>
  <blockquote>“ Nemo enim ipsam voluptatem quia voluptas sit aspernatur aut odit aut fugit, sed quia consequuntur magni dolores eos qui ratione voluptatem sequi nesiu nt. Neque porro quisqu am est, qui dolorem ipsum quia dolor sit amet, conse ctetur, adipisci velit, sed ptatem. ”</blockquote>
  <div class="author"><div class="avatar" role="img" aria-label="Portrait of the tutor"></div>LIA FONTANA</div>
  <div class="arrows">
    <svg width="20" height="20" viewBox="0 0 20 20"><circle cx="10" cy="10" r="10" fill="#fff"/><path d="M12 5 L7 10 L12 15" stroke="#0b7cc6" stroke-width="2.5" fill="none"/></svg>
    <svg width="20" height="20" viewBox="0 0 20 20"><circle cx="10" cy="10" r="10" fill="#fff"/><path d="M8 5 L13 10 L8 15" stroke="#0b7cc6" stroke-width="2.5" fill="none"/></svg>
  </div>
</section>

<section>
  <div class="blog-intro abs">
    <div class="kicker">You may be interested in</div>
    <h2>Latest<br>Blog Article</h2>
  </div>
  <div class="btn btn-red" style="left:109px;top:2855px;width:168px;height:62px">Read more</div>
  <article class="post abs" style="left:502px">
    <div class="thumb" role="img" aria-label="Woman with a dog in a clinic hallway" style="background:linear-gradient(135deg,#6f90ad,#dbe6ee 55%,#8ca8c1)"></div>
    <h3>Nemo enim ipsam voluptam quia voluptas sit</h3>
    <div class="date"><svg width="14" height="14" viewBox="0 0 14 14"><rect x="1" y="2" width="12" height="11" rx="1" fill="none" stroke="#e41d3d" stroke-width="1.5"/><path d="M1 5.5H13M4 0.5V3.5M10 0.5V3.5" stroke="#e41d3d" stroke-width="1.5"/></svg>03/04/2021</div>
  </article>
  <article class="post abs" style="left:810px">
    <div class="thumb" role="img" aria-label="Hospital building with a cross sign" style="background:linear-gradient(160deg,#c7a9b0,#a99ab5 50%,#d6d3d8)"></div>
    <h3>Nemo enim ipsam voluptam quia voluptas sit</h3>
    <div class="date"><svg width="14" height="14" viewBox="0 0 14 14"><rect x="1" y="2" width="12" height="11" rx="1" fill="none" stroke="#e41d3d" stroke-width="1.5"/><path d="M1 5.5H13M4 0.5V3.5M10 0.5V3.5" stroke="#e41d3d" stroke-width="1.5"/></svg>03/04/2021</div>
  </article>
</section>

<footer>
  <svg class="footer-bg abs" width="1200" height="610" viewBox="0 0 1200 610">
    <path d="M0 2 C120 60 250 110 420 110 C620 110 720 20 900 26 C1040 30 1130 80 1200 110 L1200 610 L0 610 Z" fill="#0e0e0f"/>
  </svg>
  <div class="brand footer-brand abs">Vela Pet <i></i></div>
  <div class="footer-about abs">
    <p>Veterinary medical care of complete and affordable quality.</p>
    <p class="line" style="margin-top:10px"><svg width="13" height="13" viewBox="0 0 24 24"><path d="M6.6 10.8a15 15 0 0 0 6.6 6.6l2.2-2.2a1 1 0 0 1 1-.25 11 11 0 0 0 3.6.6 1 1 0 0 1 1 1V20a1 1 0 0 1-1 1A17 17 0 0 1 3 4a1 1 0 0 1 1-1h3.5a1 1 0 0 1 1 1c0 1.25.2 2.45.6 3.6a1 1 0 0 1-.25 1Z" fill="#fff"/></svg>+55 21 3300-4417</p>
    <p class="line"><svg width="13" height="13" viewBox="0 0 24 24"><path d="M6.6 10.8a15 15 0 0 0 6.6 6.6l2.2-2.2a1 1 0 0 1 1-.25 11 11 0 0 0 3.6.6 1 1 0 0 1 1 1V20a1 1 0 0 1-1 1A17 17 0 0 1 3 4a1 1 0 0 1 1-1h3.5a1 1 0 0 1 1 1c0 1.25.2 2.45.6 3.6a1 1 0 0 1-.25 1Z" fill="#fff"/></svg>+55 21 97512-6638</p>
    <p>Technical manager</p>
    <p>Dr. Renato Valis - Veterinary Doctor - CRMV-RJ 00000</p>
  </div>
  <div class="fcol abs" style="left:442px"><h4>Services</h4><ul><li>Emergency Room</li><li>Queries</li><li>Exams</li><li>Vaccines</li><li>Surgeries</li></ul></div>
  <div class="fcol abs" style="left:633px"><h4>Vela Pet</h4><ul><li>Units</li><li>Blog</li><li>Work with us</li><li>Who we are</li></ul></div>
  <div class="fcol abs" style="left:784px"><h4>Help</h4><ul><li>Ombudsman</li><li>Contact us</li></ul></div>
  <div class="fcol abs" style="left:937px"><h4>Tutors</h4><ul><li>Tutor area</li><li>Schedules</li><li>Examination results</li></ul></div>
  <div class="footer-rule abs"></div>
  <p class="copyright abs">Copyright © 2021 Vela Pet. All rights reserved.</p>
  <div class="follow abs"><span>Follow us on</span><i></i><i></i><i></i><i></i></div>
</footer>

</body>
</html>
```